Lernpfad-Muster für Großhändler (interne Verwendung)
Zielgruppe
Die KORVAN Handelsbedarf Deutschland GmbH ist als Teil der KORVAN Group Großhändler und richtet sich mit seinem Sortiment an Gewerbetreibende. Um 'Profi für Profi' zu sein (und zu bleiben), ist konstante Weiterbildung wichtig. Dafür haben die Mitarbeiter - je nach Position - einen umfangreichen Lernpfad, der aus Trainings und Online-Modulen (eLearnings, Webinare...) besteht und aus dem sie frei ihre Weiterbildungsangebote wählen können.
Diese Lernpfade sollen bekannter werden, v.a. neue Kollegen sollen schon am ersten Tag wissen, was sie tun können, um ihren neuen Arbeitgeber, die Kundengruppen, die Produkte, die Strategie etc. kennenzulernen. Azubis sollen hier eine Art 'Lehrplan' vorfinden. Abnehmer sollen auch alle langjährigen Mitarbeiter und auch deren Führungskräfte sein, um Weiterbildung zu besprechen und gezielt zu planen.
Wir wünschen uns von Ihnen ein Muster, das wir nutzen können, um die Lernpfade entsprechend den Positionen auszugestalten. Beispiel: Wir würden gerne Ihr Muster nehmen und daraus ein Angebot für Kassierer und für Menschen am Wareneingang stricken (unterschiedliche Vorschläge für Trainings und eLearnings).
Die Lernpfade werden übers Intranet zur Verfügung gestellt, den Vertragsunterlagen beigelegt (geplant) und über E-Mailverteiler an Schlüsselpersonen weitergegeben.
Das Thema ist eine Fortsetzung der Training-Kampagne (Poster hängt neben weiteren Dokumenten an).
Aufgabenstellung
Die Flyer werden ausschließlich intern verwendet.
Variante: sechsseitiger Wickelpfalz oder in der Mitte geknickt (also vier Seiten)
Größe: A4
Gesetzte Seiten:
Titelseite:
Bitte den Werkelbert verwenden, das Korvan-Logo, das HR-Logo, einen beispielhaften Lernpfad-Titel (z.B. "Mitarbeiter Verkauf" oder "Abteilungsleiter Warenannahme")
Seite Trainings:
Auf einen Blick soll hier ersichtlich sein, dass es sich um Trainings handelt. Großes Piktogramm, Schraffur - wie auch immer.
Piktogramme oder kleine Bildchen (existieren noch nicht; z.B. für Rhetorik, Veränderung, Konflikt, Führung) mit Trainingstitel (z.B. "Führung konkret") und Dauer (1 Tag z.B.). 30 dieser Bildchen müssen auf eine Seite passen.
Farbliche Kennzeichnung: Führung (violett), Produkte (gelb), Systeme (grün), Soft Skills (blau); zur Einarbeitung empfohlene Trainings werden zusätzlich mit einem Sternchen, verpflichtende Trainings zusätzlich mit einem Ausrufezeichen versehen.
Seite Online-Trainings:
Auf einen Blick soll hier ersichtlich sein, dass es sich um Online-Trainings handelt. Großes Piktogramm, Schraffur - wie auch immer.
Piktogramme oder kleine Bildchen (liegen vor; z.B. für LMIV, Hygiene, Arbeitsrecht, Unsere Kunden) mit Trainingstitel und Dauer (30 Minuten z.B.). 30 dieser Bildchen müssen auf eine Seite passen.
Farbliche Kennzeichnung: wie oben

```html
<!DOCTYPE html>
<html lang="de">
<head>
<meta charset="utf-8">
<title>Lernpfad – Trainings und Online-Trainings</title>
<link rel="stylesheet" href="https://fonts.googleapis.com/css2?family=Open+Sans:wght@400;700;800&display=swap">
<style>
  :root {
    --paper: #f0f0f0;
    --ink: #3a3a3a;
    --headline: #0b22e6;
    --tile: #ffffff;
    --marker: #4f4f4f;
    --laptop: #6a6a6a;
    --products: #f4ec00;
    --leadership: #5a10e6;
    --softskills: #1739d8;
    --systems: #22c50a;
  }
  * { box-sizing: border-box; margin: 0; padding: 0; }
  html, body {
    width: 1200px; height: 851px; overflow: hidden;
    background: var(--paper);
  }
  .spread {
    position: relative;
    width: 1119px; height: 794px;
    transform: scale(1.0724);
    transform-origin: 0 0;
    font-family: "Open Sans", Arial, sans-serif;
    color: var(--ink);
  }
  .page { position: absolute; top: 0; width: 560px; height: 794px; }
  .page--training { left: 0; }
  .page--online { left: 566px; }

  .page__header { position: absolute; top: 28px; left: 22px; display: flex; align-items: center; }
  .page__symbol { width: 66px; height: 52px; display: block; }
  .page__title {
    margin-left: 15px;
    font-size: 26px; font-weight: 800; letter-spacing: 3.2px;
    color: var(--headline);
  }
  .page--online .page__title { margin-left: 24px; }

  .course-list {
    position: absolute; top: 122px; left: 22px;
    list-style: none;
    display: grid;
    grid-template-columns: 256px 256px;
    grid-template-rows: repeat(15, 40px);
    grid-auto-flow: column;
  }
  .course { position: relative; height: 40px; }
  .course__icon {
    position: absolute; left: 0; top: 0;
    width: 27px; height: 27px;
  }
  .course__title {
    position: absolute; left: 37px; top: 0; width: 170px;
    font-size: 10.6px; line-height: 13px;
  }
  .course__time {
    position: absolute; left: 209px; top: 0;
    font-size: 10.6px; line-height: 13px;
  }
  .course--products { color: var(--products); }
  .course--leadership { color: var(--leadership); }
  .course--softskills { color: var(--softskills); }
  .course--systems { color: var(--systems); }
  .course .course__title, .course .course__time { color: var(--ink); }
</style>
</head>
<body>
<svg width="0" height="0" style="position:absolute">
  <defs>
    <symbol id="ic-person" viewBox="0 0 26 26">
      <rect width="26" height="26" fill="var(--tile)"/>
      <circle cx="13" cy="10" r="4.8" fill="currentColor"/>
      <path d="M5 24 Q5 15.5 13 15.5 Q21 15.5 21 24 Z" fill="currentColor"/>
    </symbol>
    <symbol id="ic-speaker" viewBox="0 0 26 26">
      <rect width="26" height="26" fill="var(--tile)"/>
      <circle cx="10" cy="11" r="4.5" fill="currentColor"/>
      <path d="M3 24 Q3 16 10 16 Q17 16 17 24 Z" fill="currentColor"/>
      <rect x="13" y="1.5" width="11" height="6.5" rx="3" fill="currentColor"/>
    </symbol>
    <symbol id="ic-zigzag" viewBox="0 0 26 26">
      <rect width="26" height="26" fill="var(--tile)"/>
      <polyline points="9,3 15,10 10,15 15,21" fill="none" stroke="currentColor" stroke-width="1.6"/>
      <polygon points="10.5,23.5 16.5,18 13,17.5" fill="currentColor"/>
    </symbol>
    <symbol id="ic-trend" viewBox="0 0 26 26">
      <rect width="26" height="26" fill="var(--tile)"/>
      <polyline points="3,20 9,14 13,17 20,10" fill="none" stroke="currentColor" stroke-width="1.6"/>
      <polygon points="22.5,7 16,8.5 21,13" fill="currentColor"/>
    </symbol>
  </defs>
</svg>

<main class="spread">
  <section class="page page--training">
    <header class="page__header">
      <svg class="page__symbol" viewBox="0 0 66 52" aria-hidden="true">
        <rect x="8" y="1" width="50" height="50" fill="var(--marker)"/>
      </svg>
      <h1 class="page__title">TRAINING</h1>
    </header>
    <ul class="course-list">
      <li class="course course--products"><svg class="course__icon"><use href="#ic-speaker"/></svg><span class="course__title">Rhetorik:: Compliance - Geschäftsgrundsätze</span><span class="course__time">1,5h</span></li>
      <li class="course course--products"><svg class="course__icon"><use href="#ic-person"/></svg><span class="course__title">Führung: Gleichberechtigung am Arbeitsplatz</span><span class="course__time">1h</span></li>
      <li class="course course--products"><svg class="course__icon"><use href="#ic-trend"/></svg><span class="course__title">Veränderung: Arbeitsrecht für Auslerner</span><span class="course__time">30min</span></li>
      <li class="course course--products"><svg class="course__icon"><use href="#ic-zigzag"/></svg><span class="course__title">Konflikt: Gerechte Konfliktlösung zwischen Mitarbeitern</span><span class="course__time">30min</span></li>
      <li class="course course--leadership"><svg class="course__icon"><use href="#ic-speaker"/></svg><span class="course__title">Rhetorik:: Compliance - Geschäftsgrundsätze</span><span class="course__time">1,5h</span></li>
      <li class="course course--leadership"><svg class="course__icon"><use href="#ic-person"/></svg><span class="course__title">Führung: Gleichberechtigung am Arbeitsplatz</span><span class="course__time">1h</span></li>
      <li class="course course--leadership"><svg class="course__icon"><use href="#ic-zigzag"/></svg><span class="course__title">Veränderung: Arbeitsrecht für Auslerner</span><span class="course__time">30min</span></li>
      <li class="course course--leadership"><svg class="course__icon"><use href="#ic-trend"/></svg><span class="course__title">Konflikt: Gerechte Konfliktlösung zwischen Mitarbeitern</span><span class="course__time">30min</span></li>
      <li class="course course--softskills"><svg class="course__icon"><use href="#ic-speaker"/></svg><span class="course__title">Rhetorik:: Compliance - Geschäftsgrundsätze</span><span class="course__time">1,5h</span></li>
      <li class="course course--softskills"><svg class="course__icon"><use href="#ic-person"/></svg><span class="course__title">Führung: Gleichberechtigung am Arbeitsplatz</span><span class="course__time">1h</span></li>
      <li class="course course--softskills"><svg class="course__icon"><use href="#ic-zigzag"/></svg><span class="course__title">Veränderung: Arbeitsrecht für Auslerner</span><span class="course__time">30min</span></li>
      <li class="course course--softskills"><svg class="course__icon"><use href="#ic-trend"/></svg><span class="course__title">Konflikt: Gerechte Konfliktlösung zwischen Mitarbeitern</span><span class="course__time">30min</span></li>
      <li class="course course--systems"><svg class="course__icon"><use href="#ic-person"/></svg><span class="course__title">Rhetorik:: Compliance - Geschäftsgrundsätze</span><span class="course__time">1,5h</span></li>
      <li class="course course--systems"><svg class="course__icon"><use href="#ic-speaker"/></svg><span class="course__title">Führung: Gleichberechtigung am Arbeitsplatz</span><span class="course__time">1h</span></li>
      <li class="course course--systems"><svg class="course__icon"><use href="#ic-zigzag"/></svg><span class="course__title">Veränderung: Arbeitsrecht für Auslerner</span><span class="course__time">30min</span></li>

      <li class="course course--products"><svg class="course__icon"><use href="#ic-speaker"/></svg><span class="course__title">Rhetorik:: Compliance - Geschäftsgrundsätze</span><span class="course__time">1,5h</span></li>
      <li class="course course--products"><svg class="course__icon"><use href="#ic-person"/></svg><span class="course__title">Führung: Gleichberechtigung am Arbeitsplatz</span><span class="course__time">1h</span></li>
      <li class="course course--products"><svg class="course__icon"><use href="#ic-trend"/></svg><span class="course__title">Veränderung: Arbeitsrecht für Auslerner</span><span class="course__time">30min</span></li>
      <li class="course course--products"><svg class="course__icon"><use href="#ic-zigzag"/></svg><span class="course__title">Konflikt: Gerechte Konfliktlösung zwischen Mitarbeitern</span><span class="course__time">30min</span></li>
      <li class="course course--leadership"><svg class="course__icon"><use href="#ic-speaker"/></svg><span class="course__title">Rhetorik:: Compliance - Geschäftsgrundsätze</span><span class="course__time">1,5h</span></li>
      <li class="course course--leadership"><svg class="course__icon"><use href="#ic-person"/></svg><span class="course__title">Führung: Gleichberechtigung am Arbeitsplatz</span><span class="course__time">1h</span></li>
      <li class="course course--leadership"><svg class="course__icon"><use href="#ic-zigzag"/></svg><span class="course__title">Veränderung: Arbeitsrecht für Auslerner</span><span class="course__time">30min</span></li>
      <li class="course course--leadership"><svg class="course__icon"><use href="#ic-trend"/></svg><span class="course__title">Konflikt: Gerechte Konfliktlösung zwischen Mitarbeitern</span><span class="course__time">30min</span></li>
      <li class="course course--softskills"><svg class="course__icon"><use href="#ic-speaker"/></svg><span class="course__title">Rhetorik:: Compliance - Geschäftsgrundsätze</span><span class="course__time">1,5h</span></li>
      <li class="course course--softskills"><svg class="course__icon"><use href="#ic-person"/></svg><span class="course__title">Führung: Gleichberechtigung am Arbeitsplatz</span><span class="course__time">1h</span></li>
      <li class="course course--softskills"><svg class="course__icon"><use href="#ic-zigzag"/></svg><span class="course__title">Veränderung: Arbeitsrecht für Auslerner</span><span class="course__time">30min</span></li>
      <li class="course course--softskills"><svg class="course__icon"><use href="#ic-trend"/></svg><span class="course__title">Konflikt: Gerechte Konfliktlösung zwischen Mitarbeitern</span><span class="course__time">30min</span></li>
      <li class="course course--systems"><svg class="course__icon"><use href="#ic-person"/></svg><span class="course__title">Rhetorik:: Compliance - Geschäftsgrundsätze</span><span class="course__time">1,5h</span></li>
      <li class="course course--systems"><svg class="course__icon"><use href="#ic-speaker"/></svg><span class="course__title">Führung: Gleichberechtigung am Arbeitsplatz</span><span class="course__time">1h</span></li>
      <li class="course course--systems"><svg class="course__icon"><use href="#ic-zigzag"/></svg><span class="course__title">Veränderung: Arbeitsrecht für Auslerner</span><span class="course__time">30min</span></li>
    </ul>
  </section>

  <section class="page page--online">
    <header class="page__header">
      <svg class="page__symbol" viewBox="0 0 66 52" aria-hidden="true">
        <rect x="8" y="2" width="50" height="34" rx="2" fill="var(--laptop)"/>
        <rect x="12" y="6" width="42" height="26" fill="var(--paper)"/>
        <rect x="22" y="11" width="22" height="12" fill="var(--products)"/>
        <path d="M6 39 H60 L65 48 H1 Z" fill="var(--laptop)"/>
        <rect x="26" y="42" width="14" height="2" fill="var(--paper)"/>
      </svg>
      <h1 class="page__title">ONLINE - TRAINING</h1>
    </header>
    <ul class="course-list">
      <li class="course course--products"><svg class="course__icon"><use href="#ic-speaker"/></svg><span class="course__title">Rhetorik:: Compliance - Geschäftsgrundsätze</span><span class="course__time">1,5h</span></li>
      <li class="course course--products"><svg class="course__icon"><use href="#ic-person"/></svg><span class="course__title">Führung: Gleichberechtigung am Arbeitsplatz</span><span class="course__time">1h</span></li>
      <li class="course course--products"><svg class="course__icon"><use href="#ic-trend"/></svg><span class="course__title">Veränderung: Arbeitsrecht für Auslerner</span><span class="course__time">30min</span></li>
      <li class="course course--products"><svg class="course__icon"><use href="#ic-zigzag"/></svg><span class="course__title">Konflikt: Gerechte Konfliktlösung zwischen Mitarbeitern</span><span class="course__time">30min</span></li>
      <li class="course course--leadership"><svg class="course__icon"><use href="#ic-speaker"/></svg><span class="course__title">Rhetorik:: Compliance - Geschäftsgrundsätze</span><span class="course__time">1,5h</span></li>
      <li class="course course--leadership"><svg class="course__icon"><use href="#ic-person"/></svg><span class="course__title">Führung: Gleichberechtigung am Arbeitsplatz</span><span class="course__time">1h</span></li>
      <li class="course course--leadership"><svg class="course__icon"><use href="#ic-zigzag"/></svg><span class="course__title">Veränderung: Arbeitsrecht für Auslerner</span><span class="course__time">30min</span></li>
      <li class="course course--leadership"><svg class="course__icon"><use href="#ic-trend"/></svg><span class="course__title">Konflikt: Gerechte Konfliktlösung zwischen Mitarbeitern</span><span class="course__time">30min</span></li>
      <li class="course course--softskills"><svg class="course__icon"><use href="#ic-speaker"/></svg><span class="course__title">Rhetorik:: Compliance - Geschäftsgrundsätze</span><span class="course__time">1,5h</span></li>
      <li class="course course--softskills"><svg class="course__icon"><use href="#ic-person"/></svg><span class="course__title">Führung: Gleichberechtigung am Arbeitsplatz</span><span class="course__time">1h</span></li>
      <li class="course course--softskills"><svg class="course__icon"><use href="#ic-zigzag"/></svg><span class="course__title">Veränderung: Arbeitsrecht für Auslerner</span><span class="course__time">30min</span></li>
      <li class="course course--softskills"><svg class="course__icon"><use href="#ic-trend"/></svg><span class="course__title">Konflikt: Gerechte Konfliktlösung zwischen Mitarbeitern</span><span class="course__time">30min</span></li>
      <li class="course course--systems"><svg class="course__icon"><use href="#ic-person"/></svg><span class="course__title">Rhetorik:: Compliance - Geschäftsgrundsätze</span><span class="course__time">1,5h</span></li>
      <li class="course course--systems"><svg class="course__icon"><use href="#ic-speaker"/></svg><span class="course__title">Führung: Gleichberechtigung am Arbeitsplatz</span><span class="course__time">1h</span></li>
      <li class="course course--systems"><svg class="course__icon"><use href="#ic-zigzag"/></svg><span class="course__title">Veränderung: Arbeitsrecht für Auslerner</span><span class="course__time">30min</span></li>

      <li class="course course--products"><svg class="course__icon"><use href="#ic-speaker"/></svg><span class="course__title">Rhetorik:: Compliance - Geschäftsgrundsätze</span><span class="course__time">1,5h</span></li>
      <li class="course course--products"><svg class="course__icon"><use href="#ic-person"/></svg><span class="course__title">Führung: Gleichberechtigung am Arbeitsplatz</span><span class="course__time">1h</span></li>
      <li class="course course--products"><svg class="course__icon"><use href="#ic-trend"/></svg><span class="course__title">Veränderung: Arbeitsrecht für Auslerner</span><span class="course__time">30min</span></li>
      <li class="course course--products"><svg class="course__icon"><use href="#ic-zigzag"/></svg><span class="course__title">Konflikt: Gerechte Konfliktlösung zwischen Mitarbeitern</span><span class="course__time">30min</span></li>
      <li class="course course--leadership"><svg class="course__icon"><use href="#ic-speaker"/></svg><span class="course__title">Rhetorik:: Compliance - Geschäftsgrundsätze</span><span class="course__time">1,5h</span></li>
      <li class="course course--leadership"><svg class="course__icon"><use href="#ic-person"/></svg><span class="course__title">Führung: Gleichberechtigung am Arbeitsplatz</span><span class="course__time">1h</span></li>
      <li class="course course--leadership"><svg class="course__icon"><use href="#ic-zigzag"/></svg><span class="course__title">Veränderung: Arbeitsrecht für Auslerner</span><span class="course__time">30min</span></li>
      <li class="course course--leadership"><svg class="course__icon"><use href="#ic-trend"/></svg><span class="course__title">Konflikt: Gerechte Konfliktlösung zwischen Mitarbeitern</span><span class="course__time">30min</span></li>
      <li class="course course--softskills"><svg class="course__icon"><use href="#ic-speaker"/></svg><span class="course__title">Rhetorik:: Compliance - Geschäftsgrundsätze</span><span class="course__time">1,5h</span></li>
      <li class="course course--softskills"><svg class="course__icon"><use href="#ic-person"/></svg><span class="course__title">Führung: Gleichberechtigung am Arbeitsplatz</span><span class="course__time">1h</span></li>
      <li class="course course--softskills"><svg class="course__icon"><use href="#ic-zigzag"/></svg><span class="course__title">Veränderung: Arbeitsrecht für Auslerner</span><span class="course__time">30min</span></li>
      <li class="course course--softskills"><svg class="course__icon"><use href="#ic-trend"/></svg><span class="course__title">Konflikt: Gerechte Konfliktlösung zwischen Mitarbeitern</span><span class="course__time">30min</span></li>
      <li class="course course--systems"><svg class="course__icon"><use href="#ic-person"/></svg><span class="course__title">Rhetorik:: Compliance - Geschäftsgrundsätze</span><span class="course__time">1,5h</span></li>
      <li class="course course--systems"><svg class="course__icon"><use href="#ic-speaker"/></svg><span class="course__title">Führung: Gleichberechtigung am Arbeitsplatz</span><span class="course__time">1h</span></li>
      <li class="course course--systems"><svg class="course__icon"><use href="#ic-zigzag"/></svg><span class="course__title">Veränderung: Arbeitsrecht für Auslerner</span><span class="course__time">30min</span></li>
    </ul>
  </section>
</main>
</body>
</html>
```